Tango Holiday Website Needs a Header Design

I'm looking for a talented designer to create an attractive header for my website: http://brightmerengue.de/. I only want a Header Design. The website and everything else should stay the same.
We will be offering vacations for people who want to come to Tenerife to learn and dance Argentine tango. There will be lessons during the day and dancing during the evening. Tenerife is a warm and sunny destination.
The header should blend in well with the background and the images. The current dimentions fo the header is 960 x 160 pixels.
I like the design on a similar website: http://velosacumbia.de/.
Here are some images on google for tango holiday that might help: http://qlnk.to/7kRw41P
I'm flexible with colours and am looking forward to your suggestions.
Tango dancers between the ages of 40 and 65

```html
<!DOCTYPE html>
<html lang="en">
<head>
<meta charset="utf-8">
<title>Corvalan Dance – Warm Island Dance Breaks</title>
<link href="https://fonts.googleapis.com/css2?family=Great+Vibes&family=Cinzel:wght@400&display=swap" rel="stylesheet">
<style>
  :root {
    --sky-light: #fdf3d6;
    --sky-warm: #f8dfa6;
    --sky-deep: #f1c27e;
    --ridge: rgba(200, 140, 85, 0.38);
    --ridge-far: rgba(215, 165, 110, 0.25);
    --ink: #1b140e;
    --accent-red: #b9321d;
    --emblem: #e9822a;
  }
  html, body {
    margin: 0;
    padding: 0;
    overflow: hidden;
    background: #ffffff;
  }
  .site-header {
    position: relative;
    width: 1200px;
    height: 200px;
    overflow: hidden;
    background:
      radial-gradient(ellipse 560px 280px at 180px 50px, var(--sky-light) 0%, rgba(253,243,214,0) 70%),
      linear-gradient(180deg, var(--sky-warm) 0%, var(--sky-deep) 100%);
  }
  .site-header__ridges {
    position: absolute;
    right: 0;
    bottom: 0;
    width: 760px;
    height: 110px;
    background:
      radial-gradient(ellipse 420px 80px at 78% 100%, var(--ridge) 0%, rgba(0,0,0,0) 100%),
      radial-gradient(ellipse 540px 90px at 42% 112%, var(--ridge-far) 0%, rgba(0,0,0,0) 100%);
  }
  .brand-emblem {
    position: absolute;
    left: 137px;
    top: 50px;
    width: 138px;
    height: 138px;
    border-radius: 50%;
    background: var(--emblem);
  }
  .brand {
    position: absolute;
    left: 500px;
    top: 40px;
  }
  .brand__name {
    margin: 0;
    font-family: "Great Vibes", cursive;
    font-weight: 400;
    font-size: 86px;
    line-height: 1;
    color: var(--ink);
    letter-spacing: 2px;
    white-space: nowrap;
  }
  .brand__tagline {
    margin: 2px 0 0 2px;
    font-family: "Cinzel", serif;
    font-weight: 400;
    font-size: 18px;
    letter-spacing: 1.5px;
    color: var(--accent-red);
    white-space: nowrap;
  }
</style>
</head>
<body>
  <header class="site-header">
    <div class="site-header__ridges" role="img" aria-label="Faint silhouette of island mountains at sunset"></div>
    <div class="brand-emblem" aria-hidden="true"></div>
    <div class="brand">
      <h1 class="brand__name">Corvalan Dance</h1>
      <p class="brand__tagline">Warm Island Dance Breaks</p>
    </div>
  </header>
</body>
</html>
```